Tending Our Garden eBook Cover Design

I want to deisgn a cover for my eBook (FRONT COVER) and the title is:

What I Grew From a Single Spark. And Why It Matters
By KT Dorran

TITLE CHANGED TO: UNDER THE WILLOW TREE; WHERE I FOUND MY QUIET STRENGTH AND WHERE YOU MIGHT TOO

The color palette is attached. Along with some photos options of me. Along with the ebook in WORD Document. My website is www.KTDorranLive.example. You can use a different color palette if you think it is best

Target Market(s)

women who look to build a personal brand

Industry/Entity Type

health and wellness

Requirements
Must have
• the title
Nice to have
• use my picture on the cover; but that is optional
Should not have
• any men

```html
<!DOCTYPE html>
<html lang="en">
<head>
<meta charset="utf-8">
<title>Under the Willow Tree — KT Dorran</title>
<link rel="stylesheet" href="https://fonts.googleapis.com/css2?family=League+Spartan:wght@800;900&family=Allura&family=Kaushan+Script&display=swap">
<style>
  :root {
    --backdrop: #a9a9a9;
    --maroon: #5c262d;
    --mauve: #8a4552;
    --blush-edge: #e6c6c4;
    --blush-glow: #fbeeee;
    --gold: #d6b24c;
    --white: #ffffff;
  }
  * { box-sizing: border-box; margin: 0; padding: 0; }
  html, body { width: 838px; height: 1200px; overflow: hidden; }
  body { background: var(--backdrop); position: relative; }

  .cover {
    position: absolute; left: 107px; top: 100px;
    width: 625px; height: 1000px; overflow: hidden;
    background: radial-gradient(ellipse 60% 45% at 50% 52%, var(--blush-glow) 0%, var(--blush-edge) 100%);
    box-shadow: 0 6px 22px rgba(0,0,0,.35);
  }

  .title { position: absolute; left: 0; right: 0; text-align: center;
    font-family: "League Spartan", sans-serif; font-weight: 900; line-height: 1; white-space: nowrap; }
  .title-lead { top: 36px; font-size: 66px; color: var(--maroon); letter-spacing: 1px; }
  .title-main { top: 100px; font-size: 110px; color: var(--mauve); letter-spacing: -1px; }
  .title-end { top: 196px; font-size: 110px; color: var(--maroon); letter-spacing: -1px; }

  .coin-mark {
    display: inline-block; width: 86px; height: 86px; border-radius: 50%;
    vertical-align: -4px; background: var(--gold);
    color: transparent; overflow: hidden; line-height: 86px;
  }

  .subtitle-script {
    position: absolute; left: 0; right: 0; top: 288px; text-align: center;
    font-family: "Allura", cursive; font-size: 70px; color: var(--maroon); line-height: 1;
  }
  .subtitle-caps {
    position: absolute; left: 0; right: 0; top: 372px; text-align: center;
    font-family: "League Spartan", sans-serif; font-weight: 800;
    font-size: 37px; line-height: 40px; color: var(--mauve); white-space: nowrap;
  }

  .author-photo {
    position: absolute; left: 0; right: 0; top: 462px; height: 424px;
    background: radial-gradient(ellipse 36% 75% at 52% 78%, #2e2628 0%, #3a2f31 50%, rgba(230,198,196,0) 80%);
  }

  .byline-band {
    position: absolute; left: 0; right: 0; bottom: 0; height: 114px;
    background: var(--maroon); display: flex; align-items: center; justify-content: center;
  }
  .byline { font-family: "Kaushan Script", cursive; font-size: 44px; color: var(--white); line-height: 1; }
</style>
</head>
<body>
  <main class="cover">
    <h1>
      <span class="title title-lead">UNDER THE</span>
      <span class="title title-main">WILL<span class="coin-mark" role="img" aria-label="Gold coin standing in for the letter O">O</span>W</span>
      <span class="title title-end">TREE</span>
    </h1>
    <p class="subtitle-script">Where I Found</p>
    <p class="subtitle-caps">MY QUIET STRENGTH<br>AND WHERE YOU MIGHT TOO</p>
    <div class="author-photo" role="img" aria-label="Photo of the author smiling and waving, with banknotes floating around her"></div>
    <footer class="byline-band"><p class="byline">By KT Dorran</p></footer>
  </main>
</body>
</html>
```